High Profile Web Design Project

We need a sleek,state-of-the-art design for an international real estate company based in the Gulf region.

Fonts should be modern and clean, and a corner should in the top banner should be reserved for the logo.

The logo of the company is gold, navy blue, and white so the website should coincide with this.

The site will actually be an internal portal so it is important that the focus is on content.

This is the first of many requests. Top ten designers will be contacted repeatedly both via the site and privately for further business.

As this is an internal portal for employees, focus should be on news, policies, search, complaints, etc.
Updates

Hi All, 

More information on the requirements: 

1- Group Homepage (Do not include department  component like : Department News, Department Blog, Poll, Calendar)

·         Company Announcements

·         Qalvor in Press

·         Highlights / Achievements (Three main blocks with photos )

·         Photo Gallery

·         Quick Links (Trelvix – Pendrum – Organization Structure – Phone Directory …)

·         Navigation tabs
- Properties (Include sub links for departments)
-International (Include sub links for countries list)
-  Hospitality (Include sub links for hotels)
- Retail (Include sub links for attractions)
- Malls Group (Include sub links for malls)
- Technologies

 

2-      Department Homepage (Information technology for example but can be applied for Finance, HR, Marketing, Mall, Hotel…etc)

·         Department Announcements

·         Technology News

·         Project Office

·         Quick Links (Trelvix – Pendrum – IT Policies – Activity Calendar …)

·         Department Blog

·         Poll (Best Project – Employee of the month – Best Photography)... one poll  at time

 

Target Market(s)

real-estate employees

Industry/Entity Type

Real Estate

Requirements
Must have
• - Space in the corner for the logo (which is a square logo);
- Colors which match with navy blue & gold;
- Content centric design;
Should not have
• Scrolling - we want to try to limit the need for scrolling - especially on the portal home page.

```html
<!DOCTYPE html>
<html lang="en">
<head>
<meta charset="utf-8">
<title>The Real Estate – Employee Portal</title>
<link rel="stylesheet" href="https://fonts.googleapis.com/css2?family=Federant&family=Crimson+Text&family=PT+Sans:wght@700&family=Arimo:wght@400;700&display=swap">
<style>
  :root{
    --navy:#1c2566;
    --navy-deep:#141c52;
    --navy-ink:#1a2160;
    --gold:#d4a91c;
    --yellow:#f0e88a;
    --yellow-deep:#e4d767;
    --glow:#ece52f;
    --panel:#bdbbbe;
    --stage:#a19fa2;
    --text:#555458;
    --white:#ffffff;
  }
  *{box-sizing:border-box;margin:0;padding:0}
  html,body{width:1200px;height:1200px;overflow:hidden}
  body{position:relative;background:var(--stage);font-family:"Arimo",Arial,sans-serif}
  .banner{position:absolute;left:0;top:0;width:1200px;height:225px;
    background:radial-gradient(ellipse at 60% 0%,#34408a 0%,var(--navy) 55%,var(--navy-deep) 100%)}
  .hero{position:absolute;left:0;top:225px;width:1200px;height:312px;
    background:linear-gradient(180deg,#ffffff 0%,#ececec 45%,#c9c8ca 100%)}
  .site-title{position:absolute;left:222px;top:42px;width:660px;font-family:"Federant",serif;
    font-size:78px;line-height:96px;font-weight:400;letter-spacing:3px;white-space:nowrap;
    color:#e2e3ec;text-shadow:2px 3px 4px rgba(0,0,0,.6)}
  .logo-slot{position:absolute;left:911px;top:16px;width:178px;height:178px;
    border:4px solid var(--gold);background:var(--navy);
    display:flex;align-items:center;justify-content:center;
    font-family:"Arimo",sans-serif;font-size:40px;font-weight:400;color:var(--gold)}
  .house-art{position:absolute;left:70px;top:165px;width:430px;height:335px;
    background:linear-gradient(160deg,#f4f4f4 0%,#dcd6cf 45%,#b86a2a 70%,#c9c9c9 100%);
    border-radius:4px;box-shadow:0 6px 14px rgba(0,0,0,.25)}
  .main-nav{position:absolute;left:543px;top:209px;width:574px;height:45px;
    border-radius:14px;background:linear-gradient(180deg,#faf6b9 0%,var(--yellow) 50%,var(--yellow-deep) 100%);
    border:1px solid #c9b94a;box-shadow:0 8px 10px rgba(0,0,0,.12);display:flex;overflow:hidden}
  .main-nav a{display:flex;align-items:center;justify-content:center;
    font-family:"Arimo",sans-serif;font-size:17px;color:#3a3a3a;text-decoration:none;
    border-right:1px solid #b8a94a}
  .main-nav a:last-child{border-right:none}
  .main-nav .current{background:linear-gradient(180deg,#efe9a3,#e0d670);padding-top:6px}
  .intro{position:absolute;left:554px;top:284px;width:568px;font-family:"Crimson Text",serif;
    font-size:24px;line-height:29px;color:var(--navy-ink);letter-spacing:1.2px}
  .ln{display:block;white-space:nowrap;text-align:justify;text-align-last:justify}
  .ln.end{text-align-last:left}
  .search{position:absolute;left:752px;top:450px;width:353px;height:45px;border:2px solid #b9b8bb;
    border-radius:4px;background:#e3e3e4;font-family:"Arimo",sans-serif;font-size:22px;color:#9a9a9e;
    padding:9px 12px;letter-spacing:.8px}
  .search-btn{position:absolute;left:1074px;top:469px}
  .card{position:absolute;top:572px;height:493px;width:380px;border-radius:10px 10px 0 0;
    background:linear-gradient(180deg,var(--panel) 0%,#b5b3b6 100%);
    box-shadow:0 0 10px rgba(0,0,0,.25);padding:22px 0 0 0}
  .card h2{font-family:"PT Sans",sans-serif;font-weight:700;font-size:38px;letter-spacing:1.5px;
    color:var(--navy-ink);text-shadow:1px 2px 3px rgba(255,255,255,.5),0 1px 2px rgba(0,0,0,.3);line-height:44px}
  .card p{font-size:18.5px;line-height:20.8px;color:var(--text);letter-spacing:.2px}
  .card p strong{color:var(--white);font-weight:700}
  .news{left:20px;padding-left:22px;padding-right:20px}
  .policies{left:415px;padding-left:29px;padding-right:32px}
  .support{left:805px;padding-left:21px;padding-right:30px}
  .news p{margin-top:10px;color:#4e4d52}
  .policies h2{margin-top:6px}
  .policies p{margin-top:8px}
  .policies p + p{margin-top:28px}
  .support h2{margin-top:2px}
  .support p{margin-top:10px}
  .complaints{position:absolute;left:20px;top:280px;width:326px;height:136px;border:2px solid #a5a4a7;
    border-radius:6px;background:#bebcbf;text-align:center}
  .complaints .label{display:block;margin-top:10px;font-size:20px;color:#5a595d;letter-spacing:1px}
  .complaints .big{display:block;font-size:48px;line-height:46px;color:var(--glow);
    text-shadow:1px 1px 1px #6b6a3a,0 0 2px #555}
  .read-more{position:absolute;top:446px;width:139px;height:28px;border-radius:4px;
    background:linear-gradient(180deg,#9aa3b8 0%,#6d7890 100%);border:1px solid #5d6780;
    color:#eef0f6;font-size:12px;letter-spacing:1px;text-align:center;line-height:25px;
    box-shadow:0 2px 3px rgba(0,0,0,.3)}
  .news .read-more{left:215px}
  .policies .read-more{left:203px}
  .support .read-more{left:201px}
  .rule{position:absolute;left:0;top:1065px;width:1200px;height:7px;background:linear-gradient(180deg,#f0c52a,var(--gold))}
  .footer{position:absolute;left:0;top:1072px;width:1200px;height:128px;
    background:radial-gradient(ellipse at 50% 0%,#2a3480,var(--navy) 60%,var(--navy-deep))}
  .footer-links{position:absolute;left:0;top:24px;width:1200px;display:flex;justify-content:center}
  .footer-links a{color:var(--white);text-decoration:none;font-size:21px;letter-spacing:1px;
    padding:4px 10px;border-right:3px solid var(--white);line-height:25px}
  .footer-links a:last-child{border-right:none}
  .copyright{position:absolute;left:0;top:71px;width:1200px;text-align:center;color:var(--white);
    font-size:20px;letter-spacing:1.4px}
</style>
</head>
<body>
  <header>
    <div class="banner"></div>
    <div class="hero"></div>
    <h1 class="site-title">The Real Estate</h1>
    <div class="logo-slot">Qalvor</div>
    <div class="house-art" role="img" aria-label="Illustration of a two-storey house built from white cube tiles"></div>
    <nav class="main-nav">
      <a href="#" style="width:149px">Home</a>
      <a href="#" style="width:130px">Option 2</a>
      <a href="#" class="current" style="width:146px">Option 3</a>
      <a href="#" style="width:149px">Contact</a>
    </nav>
    <p class="intro">
      <span class="ln">Lorem ipsum dolor sit amet, consectetur ad-</span>
      <span class="ln">ipiscing elit. Vivamus mattis sagittis leo nec lob-</span>
      <span class="ln">ortis. Aliquam erat volutpat. Nunc ultrices fau-</span>
      <span class="ln">cibus porttitor. Maecenas vel porta lorem. Sed a</span>
      <span class="ln end">nibh ligula, et adipiscing purus.</span>
    </p>
    <div class="search">Search Our Site for more</div>
    <svg class="search-btn" width="60" height="60" viewBox="0 0 60 60" aria-label="Search">
      <circle cx="29" cy="29" r="28" fill="#c8c7ca"/>
      <circle cx="29" cy="29" r="23" fill="#f0c52a" stroke="#b38a10" stroke-width="2"/>
      <path d="M17 29h20M30 21l9 8-9 8" fill="none" stroke="#fff" stroke-width="4" stroke-linecap="round" stroke-linejoin="round"/>
    </svg>
  </header>

  <main>
    <section class="card news">
      <h2>NEWS</h2>
      <p>
        <span class="ln"><strong>Lorem ipsum dolor sit amet, con-</strong></span>
        <span class="ln"><strong>secte</strong>tur adipisicing elit, sed do eius-</span>
        <span class="ln">mod tempor incidi dunt ut labore et</span>
        <span class="ln">dolore magna aliqua. Ut enim ad</span>
        <span class="ln">minim veniam, quis nostrud exercita</span>
        <span class="ln">tion ullamco laboris nisi ut aliquip ex</span>
        <span class="ln">ea commodo. cidi dunt ut labore et</span>
        <span class="ln">dolore magna aliqua. Ut enim ad</span>
        <span class="ln">minim veniam, quis nostrud exercita</span>
        <span class="ln">tion ullamco laboris nisi ut aliquip ex</span>
        <span class="ln">ea commodo. Lorem ipsum dolor sit</span>
        <span class="ln">amet, consectetur adipisicing elit, sed</span>
        <span class="ln">do eiusmod tempor incidi dunt ut</span>
        <span class="ln end">labore et dolore magna aliqua.</span>
      </p>
      <div class="read-more">Read More</div>
    </section>
    <section class="card policies">
      <h2>POLICIES</h2>
      <p>
        <span class="ln"><strong>Lorem ipsum dolor</strong> sit amet,</span>
        <span class="ln">consectetur adipisicing elit, sed</span>
        <span class="ln">do eiusmod tempor incidi dunt ut</span>
        <span class="ln">labore et dolore magna aliqua. Ut</span>
        <span class="ln">enim ad minim veniam, quis nos-</span>
        <span class="ln">trud exercita tion ullamco laboris</span>
        <span class="ln">nisi ut aliquip ex ea commodo. cidi</span>
        <span class="ln end">dunt ut labore et dolore magn</span>
      </p>
      <p>
        <span class="ln"><strong>a aliqua.</strong> Ut enim ad minim</span>
        <span class="ln">veniam, quis nostrud exercita tion</span>
        <span class="ln">ullamco laboris nisi ut aliquip ex</span>
        <span class="ln">ea commodo. Lorem ipsum dolor</span>
        <span class="ln">sit amet, consectetur adipisicing</span>
        <span class="ln">elit, sed do eiusmod tempor incidi</span>
        <span class="ln">dunt ut labore et dolore magna</span>
        <span class="ln end">aliqua.</span>
      </p>
      <div class="read-more">Read More</div>
    </section>
    <section class="card support">
      <h2>OUR SUPPORT</h2>
      <p>
        <span class="ln">Lorem ipsum dolor sit amet,</span>
        <span class="ln">consectetur adipisicing elit, sed</span>
        <span class="ln">do eiusmod tempor incidi dunt</span>
        <span class="ln">ut labore et dolore magna</span>
        <span class="ln">aliqua. Ut enim ad minim</span>
        <span class="ln">veniam, quis nostrud exercita</span>
        <span class="ln">tion ullamco laboris nisi ut al-</span>
        <span class="ln">iquip ex ea commodo. cidi dunt</span>
        <span class="ln end">ut labore et dolore magn</span>
      </p>
      <div class="complaints">
        <span class="label">Post your Complaints here</span>
        <span class="big">Our Support<br>24 X 7</span>
      </div>
      <div class="read-more">Read More</div>
    </section>
  </main>

  <div class="rule"></div>
  <footer class="footer">
    <nav class="footer-links">
      <a href="#">Blog</a><a href="#">Support</a><a href="#">Solutions</a><a href="#">Testimonials</a><a href="#">Developments</a><a href="#">Projects</a><a href="#">Contact Us</a>
    </nav>
    <p class="copyright">@2012 Your Company. All Rights Reserved</p>
  </footer>
</body>
</html>
```